Stationary for Marigold Spa
Business Card, Envelope, & Letterhead
Project: Stationary for Marigold Spa
Stationary for Marigold Spa -
Creative Brief
Simple
use logo no person's name
27815 Orchard Blvd. Ste 342 San Antonio, TX 78259
hbt4726@quillpost.net
We don't have the website yet. Please do not use the email on the project. On the business card front side, we only need our logo, address, phone no. Back side will be the services that we will provide.
Acupressure, Tui Na, Deep Tissue Massage, Swedish Massage, Prenatal Massage, Reflexology, Traditional Herbal Foot Treatment

```html
<!DOCTYPE html>
<html lang="en">
<head>
<meta charset="utf-8">
<title>Marigold Spa — Business Card</title>
<link href="https://fonts.googleapis.com/css2?family=Questrial&family=Cabin:wght@500&display=swap" rel="stylesheet">
<style>
  :root {
    --backdrop: #ecebe6;
    --card: #ffffff;
    --olive: #b4bc1c;
    --olive-dark: #9aa117;
    --rule-gray: #b9b9b9;
    --text-gray: #7a7a7a;
    --text-dark: #222222;
    --stone-light: #f4f4f4;
    --stone-shade: #b8b8b8;
  }
  html, body {
    margin: 0;
    padding: 0;
    width: 1200px;
    height: 780px;
    overflow: hidden;
    background: var(--backdrop);
  }
  .canvas {
    position: relative;
    width: 1200px;
    height: 780px;
  }
  .business-card {
    position: absolute;
    left: 150px;
    top: 133px;
    width: 900px;
    height: 514px;
    background: var(--card);
    border-radius: 34px;
    overflow: hidden;
    box-shadow: 0 6px 22px rgba(0,0,0,0.12);
  }
  .header-band {
    position: absolute;
    left: 0;
    top: 0;
    width: 900px;
    height: 200px;
  }
  .brand-name {
    position: absolute;
    left: 150px;
    top: 178px;
    margin: 0;
    font-family: "Questrial", sans-serif;
    font-weight: 400;
    font-size: 70px;
    letter-spacing: -1px;
    color: var(--text-gray);
    line-height: 1;
  }
  .tagline {
    position: absolute;
    left: 238px;
    top: 262px;
    margin: 0;
    font-family: "Questrial", sans-serif;
    font-size: 29px;
    color: var(--olive-dark);
    line-height: 1;
  }
  .phone {
    position: absolute;
    left: 150px;
    top: 356px;
    display: flex;
    align-items: center;
    gap: 18px;
    font-family: "Questrial", sans-serif;
    font-size: 40px;
    color: var(--text-gray);
    line-height: 1;
  }
  .phone-icon {
    width: 36px;
    height: 36px;
  }
  .address {
    position: absolute;
    left: 150px;
    top: 428px;
    margin: 0;
    font-family: "Cabin", sans-serif;
    font-weight: 500;
    font-size: 19px;
    color: var(--text-dark);
    letter-spacing: 0.2px;
  }
</style>
</head>
<body>
<main class="canvas">
  <section class="business-card">
    <svg class="header-band" viewBox="0 0 900 200" aria-hidden="false">
      <defs>
        <linearGradient id="stoneTone" x1="0" y1="0" x2="0" y2="1">
          <stop offset="0" stop-color="var(--stone-light)"/>
          <stop offset="1" stop-color="var(--stone-shade)"/>
        </linearGradient>
      </defs>
      <path class="top-rule" d="M0 30 H900 V36 H0 Z" fill="var(--rule-gray)"/>
      <path class="olive-band" d="M0 42 H900 V104 C760 104 690 150 540 150 C400 150 320 108 180 118 C110 122 50 128 0 132 Z" fill="var(--olive)"/>
      <path class="band-edge" d="M0 140 C60 136 120 128 180 126 C320 116 400 158 540 158 C690 158 760 112 900 112" fill="none" stroke="var(--rule-gray)" stroke-width="3"/>
      <rect class="stone-row" role="img" aria-label="Row of smooth spa stones resting on the band edge" x="250" y="100" width="330" height="44" rx="22" fill="url(#stoneTone)"/>
    </svg>

    <h1 class="brand-name">Marigold Spa</h1>
    <p class="tagline">Health Relaxation</p>

    <div class="phone">
      <svg class="phone-icon" viewBox="0 0 36 36" aria-hidden="true">
        <circle cx="18" cy="18" r="16" fill="none" stroke="var(--olive)" stroke-width="3"/>
        <path d="M12 10 c-2 2 -2 6 2 11 s9 7 11 5 l1.5-1.5 -3.5-3.5 -2 1.5 c-2-1-4-3-5-5 l1.5-2 -3.5-3.5 z" fill="var(--olive)"/>
      </svg>
      <span class="phone-number">(210)555-0147</span>
    </div>

    <p class="address">27815 Orchard Blvd. Ste 342 San Antonio, TX 78259</p>
  </section>
</main>
</body>
</html>
```